Certified Notary Signing Agent Business Card Design

I need a modern, visually appealing two-sided business card for my mobile notary signing agent business which clearly communicates my certification by the Federal Signatory Guild ("FSG") and Deed Closing Method ("DCM"). It should be clean and easy to read and trust focused. While I am not committed to specific fonts and colors, I do like the colors in both my final logo and a sample logo (color examples only). I want to hand out a business card that is easy to locate in a stack and differentiates itself easily from others as it is an extremely crowded market space.

Target Market(s)

Title Companies, Escrow Officers, Real Estate Agents, Real Estate Lenders

Industry/Entity Type

Real Estate Lending

Contact Information for Business Card

I need a two-sided business card for my mobile notary signing agent business that prominently displays my photo, logo (potentially, just on the back), my service areas, phone, email, url and an FSG certification and DCM certification. On the back side of the card I would like my url, logo and potentially certification icons. On the back, I MAY want to add language that I have been an FSG Certified NSA for 10 + years and have performed over 8k in real estate loan transactions. I have attached a very old biz card circa 2007 that I designed myself on a card ordering platform. While it's not great, it can display how I crammed all of the data on a single card. I am NOT suggesting replicating this design in any form but provide it as reference material only,

Font styles to use
Sans Serif

Requirements
Must have
• Name: Mara Oltvany, Certified Notary Signing Agent Phone: 936.482.1795 URL: www.TopTierSealers.example Email: mara@toptiersealers.example, Counties serviced: Montgomery, Grimes, N. Harris, Walker, Waller, Federal Signatory Guild Badge, Deed Closing Method Badge (still need to upload this)
Nice to have
• I am open to color variations on my logo as illustrated in the attachment labeled as Logo Sample Colors Only (11A) that has a slate blue/grey background w/white lettering and gold pen and circles

```html
<!DOCTYPE html>
<html lang="en">
<head>
<meta charset="utf-8">
<title>Mara Oltvany – Business Card</title>
<link href="https://fonts.googleapis.com/css2?family=Poppins:wght@400;600&family=EB+Garamond:ital,wght@1,500&display=swap" rel="stylesheet">
<style>
  :root {
    --bg: #2a2a2a;
    --card: #131313;
    --card-back: #101010;
    --gold: #e39b35;
    --white: #f4f4f4;
    --rule: #8a8a8a;
    --navy: #1e4f8f;
    --badge-red: #d8343b;
    --cream: #f6ecd7;
  }
  * { margin: 0; padding: 0; box-sizing: border-box; }
  html, body { width: 1200px; height: 1108px; overflow: hidden; }
  body {
    background: var(--bg);
    font-family: "Poppins", sans-serif;
    color: var(--white);
    position: relative;
  }
  .card {
    position: absolute;
    top: 194px;
    width: 410px;
    height: 720px;
    border-radius: 22px;
    overflow: hidden;
  }
  .card-front { left: 160px; background: var(--card); text-align: center; }
  .card-back { left: 630px; background: var(--card-back); text-align: center; }

  /* Front */
  .portrait {
    width: 224px; height: 224px; border-radius: 50%;
    margin: 62px auto 0;
    border: 2px solid var(--gold);
    background: radial-gradient(circle at 50% 45%, #c9a27a 0 28%, #8a6a4c 45%, #353535 70%);
  }
  .name {
    margin-top: 26px;
    color: var(--gold); font-weight: 600; font-size: 25px; letter-spacing: .5px;
    text-transform: uppercase; line-height: 1.1;
  }
  .title { font-size: 17px; margin-top: 2px; }
  .icon-row {
    display: flex; align-items: center; justify-content: center; gap: 7px;
    margin: 16px 40px 0;
  }
  .icon-row .rule { flex: 1; height: 1px; background: var(--rule); }
  .icon {
    width: 27px; height: 27px; border-radius: 5px; background: var(--gold);
    display: flex; align-items: center; justify-content: center;
  }
  .contact { margin-top: 10px; font-size: 17px; line-height: 1.3; }
  .divider { height: 1px; background: var(--rule); margin: 20px 62px 18px; }
  .label { color: var(--gold); font-weight: 600; font-size: 19px; text-transform: uppercase; }
  .counties { font-size: 17px; line-height: 1.3; margin-top: 2px; }
  .credentials {
    display: flex; align-items: center; justify-content: center; gap: 14px;
    margin-top: 26px;
  }
  .partner { display: flex; align-items: center; gap: 8px; }
  .partner-dot { width: 44px; height: 44px; border-radius: 50%; background: var(--navy); }
  .partner-name { color: var(--navy); font-size: 14px; line-height: 1.05; text-align: left; width: 70px; }
  .seal { width: 50px; height: 50px; border-radius: 50%; background: var(--badge-red); border: 5px solid var(--white); }

  /* Back */
  .back-texture {
    position: absolute; inset: 0;
    background: linear-gradient(160deg, #1c1c1c 0%, #121212 50%, #0c0c0c 100%);
  }
  .back-content { position: relative; }
  .brand {
    width: 176px; height: 176px; border-radius: 50%;
    margin: 110px auto 0;
    background: var(--cream); border: 6px solid var(--gold);
    display: flex; align-items: center; justify-content: center;
    color: #1a1a1a; font-weight: 600; font-size: 20px; line-height: 1.15;
    text-transform: uppercase; padding: 0 18px;
  }
  .statement {
    margin: 58px 50px 0;
    font-family: "EB Garamond", serif; font-style: italic; font-weight: 500;
    font-size: 22px; line-height: 1.25;
  }
  .back-url { color: var(--gold); font-size: 18px; margin-top: 16px; }
  .cert-seal {
    width: 104px; height: 104px; border-radius: 50%;
    margin: 60px auto 0;
    background: var(--white); border: 8px solid var(--badge-red);
  }
</style>
</head>
<body>

<section class="card card-front">
  <div class="portrait" role="img" aria-label="Portrait photo of Mara Oltvany"></div>
  <h1 class="name">Mara Oltvany</h1>
  <p class="title">Certified Notary Signing Agent</p>
  <div class="icon-row">
    <span class="rule"></span>
    <span class="icon"><svg width="15" height="15" viewBox="0 0 24 24"><path fill="#fff" d="M6.6 10.8a15 15 0 0 0 6.6 6.6l2.2-2.2a1 1 0 0 1 1-.25 11.4 11.4 0 0 0 3.6.6 1 1 0 0 1 1 1V20a1 1 0 0 1-1 1A17 17 0 0 1 3 4a1 1 0 0 1 1-1h3.5a1 1 0 0 1 1 1c0 1.25.2 2.45.6 3.6a1 1 0 0 1-.25 1z"/></svg></span>
    <span class="icon"><svg width="16" height="13" viewBox="0 0 24 18"><rect x="1" y="1" width="22" height="16" fill="none" stroke="#fff" stroke-width="2"/><path d="M1 1l11 9 11-9" fill="none" stroke="#fff" stroke-width="2"/></svg></span>
    <span class="icon"><svg width="15" height="15" viewBox="0 0 24 24"><circle cx="12" cy="12" r="10" fill="none" stroke="#fff" stroke-width="2"/><path d="M2 12h20M12 2c3 3 3 17 0 20M12 2c-3 3-3 17 0 20" fill="none" stroke="#fff" stroke-width="1.6"/></svg></span>
    <span class="rule"></span>
  </div>
  <p class="contact">936.482.1795<br>www.TopTierSealers.example<br>mara@toptiersealers.example</p>
  <div class="divider"></div>
  <p class="label">Counties Serviced</p>
  <p class="counties">Montgomery, Grimes, N. Harris,<br>Walker, Waller</p>
  <div class="credentials">
    <div class="partner">
      <span class="partner-dot"></span>
      <span class="partner-name">Deed Closing Method</span>
    </div>
    <span class="seal" role="img" aria-label="Federal Signatory Guild certification badge"></span>
  </div>
</section>

<section class="card card-back">
  <div class="back-texture" role="img" aria-label="Faint repeating house and pen pattern"></div>
  <div class="back-content">
    <div class="brand">Top Tier Sealers</div>
    <p class="statement">FSG Certified NSA for 10 + years and have performed over 8k in real estate loan transactions.</p>
    <p class="back-url">www.TopTierSealers.example</p>
    <div class="cert-seal" role="img" aria-label="Federal Signatory Guild certified signing agent badge"></div>
  </div>
</section>

</body>
</html>
```